Networking Events Calendar/Diary

We need a responsive website that can act as both an online diary/calendar and a resource for community and networking events similar to mingleroundsplaza.com (we do not want a clone, but one with similar functionality). We need to be able to host adverts, have a client area for clients to add their own events to the diary. This needs to have the functionality that clients have to pay to add recurring events. Some integration would be useful so that if a clients already has their own online diary on their website then using an API possibly to also add that event into our online diary

Industry/Entity Type

Events

Coding

Coded - Design and coding required

Number of Pages Required

5+ page

Requirements
Must have
• My project must have a calendar area, space for ads, be responsive and easily viewable on mobile. A subscribers area for clients and a way to purchase premium status so that premium events are highlighted.

```html
<!DOCTYPE html>
<html lang="en">
<head>
<meta charset="utf-8">
<title>Meetwell Diary – Events Calendar</title>
<link rel="stylesheet" href="https://fonts.googleapis.com/css2?family=Open+Sans:wght@300;400;600;700&family=PT+Sans+Narrow:wght@400;700&display=swap">
<style>
:root{
  --plum:#8d4275;
  --rose:#ee5463;
  --tangerine:#ff7a33;
  --orange:#f28a14;
  --grey-box:#ababab;
  --ink:#222;
  --muted:#555;
  --nav-bg:#f0f0f0;
  --ad-bg:#f4f4f4;
  --white:#fff;
}
*{box-sizing:border-box;margin:0;padding:0}
html,body{width:1200px;height:2550px;overflow:hidden;background:var(--white);font-family:"Open Sans",Arial,sans-serif;color:var(--ink)}
.page{position:relative;width:1200px;height:2550px}

/* Header */
.hero{position:absolute;left:0;top:0;width:1200px;height:505px;background:linear-gradient(90deg,var(--plum) 0%,#c44a6a 30%,var(--rose) 50%,#fa6a45 75%,var(--tangerine) 100%);color:var(--white)}
.brand{position:absolute;left:173px;top:68px;display:flex;align-items:center;gap:18px}
.brand-mark{width:48px;height:48px;border:5px solid var(--white);border-radius:6px}
.brand-name{font-family:"PT Sans Narrow","Arial Narrow",sans-serif;font-weight:700;font-size:42px;letter-spacing:.5px;text-transform:uppercase}
.welcome{position:absolute;left:173px;top:183px;width:380px;font-size:14.5px;line-height:24px;font-weight:300}
.welcome strong{font-weight:600;display:block}
.hero-link{position:absolute;left:173px;display:flex;align-items:center;gap:18px;font-size:14.5px;font-weight:600}
.hero-link svg{width:26px;height:26px}

/* Calendar */
.calendar{position:absolute;left:668px;top:62px;width:354px}
.cal-head{display:flex;justify-content:space-between;align-items:center;font-family:"PT Sans Narrow","Arial Narrow",sans-serif;font-weight:700;text-transform:uppercase}
.cal-title{font-size:17px}
.cal-create{font-size:11px;display:flex;align-items:center;gap:7px}
.cal-controls{display:flex;align-items:center;margin-top:20px;gap:14px}
.cal-controls svg{width:14px;height:14px}
.btn-today{border:1.5px solid var(--white);border-radius:5px;font-size:9.5px;font-weight:700;padding:3px 8px;font-family:"PT Sans Narrow",sans-serif}
.cal-month{font-family:"PT Sans Narrow",sans-serif;font-weight:700;font-size:15.5px;margin-left:4px}
.view-switch{margin-left:auto;display:flex;border:1px solid var(--white);border-radius:3px;overflow:hidden;font-size:10px}
.view-switch span{padding:3px 7px;border-left:1px solid var(--white)}
.view-switch span:first-child{border-left:none;background:var(--white);color:var(--rose)}
.cal-grid{display:grid;grid-template-columns:repeat(7,1fr);margin-top:20px;margin-left:-14px;width:382px;text-align:center;font-size:14px}
.cal-grid .dow{font-weight:700;font-size:13px;height:44px}
.cal-grid .day{height:54px;display:flex;justify-content:center}
.cal-grid .day span{width:30px;height:30px;line-height:30px;border-radius:50%;margin-top:-6px}
.cal-grid .faded{opacity:.6}
.cal-grid .today span{background:var(--white);color:var(--rose);font-weight:600}
.cal-grid .marked span{border:1.3px solid var(--white)}

/* Navigation */
.main-nav{position:absolute;left:0;top:505px;width:1200px;height:53px;background:var(--nav-bg)}
.main-nav a{position:absolute;top:18px;transform:translateX(-50%);font-size:12.5px;color:var(--muted);text-decoration:none;white-space:nowrap}

/* Sections */
.section-title{position:absolute;display:flex;align-items:center;gap:12px;font-weight:700;font-size:17px;text-transform:uppercase}
.section-title svg{width:20px;height:20px}
.event{position:absolute;left:173px;width:520px;display:flex;gap:19px}
.date-box{width:72px;height:70px;border-radius:4px;overflow:hidden;color:var(--white);text-align:center;flex:none}
.date-box .mon{height:27px;line-height:27px;font-size:15px;border-bottom:2px solid var(--white)}
.date-box .num{height:43px;line-height:42px;font-size:27px;font-weight:700}
.premium .date-box{background:var(--orange)}
.standard .date-box{background:var(--grey-box)}
.event-title{font-size:14px;font-weight:600;margin-top:-4px}
.event-meta{display:flex;align-items:center;gap:8px;font-size:11px;color:var(--muted);margin-top:9px}
.event-meta+.event-meta{margin-top:5px}
.event-meta svg{width:12px;height:12px;flex:none}

.ad-slot{position:absolute;left:734px;top:670px;width:294px;height:197px;background:var(--ad-bg)}
.promo-lead{position:absolute;left:734px;top:946px;width:290px;color:var(--orange);font-weight:600;font-size:13.5px;line-height:20px}
.promo-body{position:absolute;left:734px;top:1003px;width:300px;font-size:13.5px;line-height:19.5px}
.btn-outline{position:absolute;left:734px;top:1103px;width:148px;height:38px;border:1.5px solid #f7b26a;border-radius:4px;color:var(--orange);font-size:13.5px;display:flex;align-items:center;justify-content:center}
</style>
</head>
<body>
<div class="page">
  <header class="hero">
    <div class="brand"><div class="brand-mark"></div><span class="brand-name">Meetwell Diary</span></div>
    <p class="welcome"><strong>Welcome to Meetwell Diary</strong>Welcome to the online resource offering a simple, quick way to access information about Business Networking Events, Business Clubs, Workshops, Seminars and Business Shows happening in your local area.</p>
    <div class="hero-link" style="top:357px">
      <svg viewBox="0 0 26 26"><circle cx="13" cy="13" r="11.5" fill="none" stroke="#fff" stroke-width="2.2"/><path d="M13 7v12M7 13h12" stroke="#fff" stroke-width="2.4"/></svg>
      Register to Add Events</div>
    <div class="hero-link" style="top:406px">
      <svg viewBox="0 0 26 26"><circle cx="5" cy="21" r="3" fill="#fff"/><path d="M2 12a12 12 0 0 1 12 12M2 4a20 20 0 0 1 20 20" fill="none" stroke="#fff" stroke-width="3.2"/></svg>
      Subscribe to our Event Bulletin</div>

    <section class="calendar">
      <div class="cal-head"><span class="cal-title">Events Calendar</span>
        <span class="cal-create">Create your event <svg width="17" height="17" viewBox="0 0 17 17"><circle cx="8.5" cy="8.5" r="7.5" fill="none" stroke="#fff" stroke-width="1.4"/><path d="M8.5 5v7M5 8.5h7" stroke="#fff" stroke-width="1.5"/></svg></span></div>
      <div class="cal-controls">
        <svg viewBox="0 0 14 14"><path d="M9.5 2 4.5 7l5 5" fill="none" stroke="#fff" stroke-width="2"/></svg>
        <svg viewBox="0 0 14 14"><path d="M4.5 2l5 5-5 5" fill="none" stroke="#fff" stroke-width="2"/></svg>
        <span class="btn-today">TODAY</span>
        <span class="cal-month">September 2015</span>
        <div class="view-switch"><span>Month</span><span>Week</span><span>Day</span></div>
      </div>
      <div class="cal-grid">
        <div class="dow">S</div><div class="dow">M</div><div class="dow">T</div><div class="dow">W</div><div class="dow">T</div><div class="dow">F</div><div class="dow">S</div>
        <div class="day faded"><span>29</span></div><div class="day faded"><span>30</span></div><div class="day today"><span>1</span></div><div class="day"><span>2</span></div><div class="day"><span>3</span></div><div class="day"><span>4</span></div><div class="day"><span>5</span></div>
        <div class="day"><span>6</span></div><div class="day"><span>7</span></div><div class="day"><span>8</span></div><div class="day marked"><span>9</span></div><div class="day"><span>10</span></div><div class="day"><span>11</span></div><div class="day"><span>12</span></div>
        <div class="day"><span>13</span></div><div class="day"><span>14</span></div><div class="day marked"><span>15</span></div><div class="day"><span>16</span></div><div class="day"><span>17</span></div><div class="day"><span>18</span></div><div class="day"><span>19</span></div>
        <div class="day"><span>20</span></div><div class="day"><span>21</span></div><div class="day"><span>22</span></div><div class="day"><span>23</span></div><div class="day"><span>24</span></div><div class="day"><span>25</span></div><div class="day"><span>26</span></div>
        <div class="day"><span>27</span></div><div class="day"><span>28</span></div><div class="day"><span>29</span></div><div class="day"><span>30</span></div><div class="day"><span>31</span></div><div class="day"><span>1</span></div><div class="day"><span>2</span></div>
      </div>
    </section>
  </header>

  <nav class="main-nav">
    <a style="left:255px">Homepage</a><a style="left:374px">What we do</a><a style="left:534px">Events by location/Region</a><a style="left:707px">Business Shows</a><a style="left:831px">Concerts</a><a style="left:944px">Contact Us</a>
  </nav>

  <h2 class="section-title" style="left:173px;top:605px"><svg viewBox="0 0 20 20"><rect x="2" y="4" width="16" height="14" rx="2" fill="none" stroke="#f28a14" stroke-width="2"/><path d="M6 2v4M14 2v4M2 8h16" stroke="#f28a14" stroke-width="2"/><rect x="8" y="11" width="4" height="4" fill="#f28a14"/></svg>Premium Events</h2>

  <article class="event premium" style="top:670px"><div class="date-box"><div class="mon">DEC</div><div class="num">13</div></div><div><h3 class="event-title">Brew &amp; Connect - Elmbridge Market</h3><p class="event-meta"><svg viewBox="0 0 12 12"><circle cx="6" cy="6" r="5" fill="none" stroke="#333" stroke-width="1.2"/><path d="M6 3v3h2.5" fill="none" stroke="#333" stroke-width="1.2"/></svg>Tuesday ,10:00am - 11:30am</p><p class="event-meta"><svg viewBox="0 0 12 12"><path d="M6 11.5S2 7 2 4.5a4 4 0 0 1 8 0C10 7 6 11.5 6 11.5z" fill="#333"/><circle cx="6" cy="4.5" r="1.4" fill="#fff"/></svg>Elmbridge Market, Ferry Lane , Elmbridge , Elmbridge , EB4 7QT</p></div></article>
  <article class="event premium" style="top:772px"><div class="date-box"><div class="mon">DEC</div><div class="num">13</div></div><div><h3 class="event-title">Brew &amp; Connect - Elmbridge Market</h3><p class="event-meta"><svg viewBox="0 0 12 12"><circle cx="6" cy="6" r="5" fill="none" stroke="#333" stroke-width="1.2"/><path d="M6 3v3h2.5" fill="none" stroke="#333" stroke-width="1.2"/></svg>Tuesday ,10:00am - 11:30am</p><p class="event-meta"><svg viewBox="0 0 12 12"><path d="M6 11.5S2 7 2 4.5a4 4 0 0 1 8 0C10 7 6 11.5 6 11.5z" fill="#333"/><circle cx="6" cy="4.5" r="1.4" fill="#fff"/></svg>Elmbridge Market, Ferry Lane , Elmbridge , Elmbridge , EB4 7QT</p></div></article>
  <article class="event premium" style="top:871px"><div class="date-box"><div class="mon">DEC</div><div class="num">13</div></div><div><h3 class="event-title">Brew &amp; Connect - Elmbridge Market</h3><p class="event-meta"><svg viewBox="0 0 12 12"><circle cx="6" cy="6" r="5" fill="none" stroke="#333" stroke-width="1.2"/><path d="M6 3v3h2.5" fill="none" stroke="#333" stroke-width="1.2"/></svg>Tuesday ,10:00am - 11:30am</p><p class="event-meta"><svg viewBox="0 0 12 12"><path d="M6 11.5S2 7 2 4.5a4 4 0 0 1 8 0C10 7 6 11.5 6 11.5z" fill="#333"/><circle cx="6" cy="4.5" r="1.4" fill="#fff"/></svg>Elmbridge Market, Ferry Lane , Elmbridge , Elmbridge , EB4 7QT</p></div></article>
  <article class="event premium" style="top:973px"><div class="date-box"><div class="mon">DEC</div><div class="num">13</div></div><div><h3 class="event-title">Brew &amp; Connect - Elmbridge Market</h3><p class="event-meta"><svg viewBox="0 0 12 12"><circle cx="6" cy="6" r="5" fill="none" stroke="#333" stroke-width="1.2"/><path d="M6 3v3h2.5" fill="none" stroke="#333" stroke-width="1.2"/></svg>Tuesday ,10:00am - 11:30am</p><p class="event-meta"><svg viewBox="0 0 12 12"><path d="M6 11.5S2 7 2 4.5a4 4 0 0 1 8 0C10 7 6 11.5 6 11.5z" fill="#333"/><circle cx="6" cy="4.5" r="1.4" fill="#fff"/></svg>Elmbridge Market, Ferry Lane , Elmbridge , Elmbridge , EB4 7QT</p></div></article>
  <article class="event premium" style="top:1078px"><div class="date-box"><div class="mon">DEC</div><div class="num">13</div></div><div><h3 class="event-title">Brew &amp; Connect - Elmbridge Market</h3><p class="event-meta"><svg viewBox="0 0 12 12"><circle cx="6" cy="6" r="5" fill="none" stroke="#333" stroke-width="1.2"/><path d="M6 3v3h2.5" fill="none" stroke="#333" stroke-width="1.2"/></svg>Tuesday ,10:00am - 11:30am</p><p class="event-meta"><svg viewBox="0 0 12 12"><path d="M6 11.5S2 7 2 4.5a4 4 0 0 1 8 0C10 7 6 11.5 6 11.5z" fill="#333"/><circle cx="6" cy="4.5" r="1.4" fill="#fff"/></svg>Elmbridge Market, Ferry Lane , Elmbridge , Elmbridge , EB4 7QT</p></div></article>

  <h2 class="section-title" style="left:173px;top:1192px"><svg viewBox="0 0 20 20"><rect x="2" y="4" width="16" height="14" rx="2" fill="none" stroke="#999" stroke-width="2"/><path d="M6 2v4M14 2v4M2 8h16" stroke="#999" stroke-width="2"/><rect x="8" y="11" width="4" height="4" fill="#999"/></svg>Events</h2>

  <article class="event standard" style="top:1258px"><div class="date-box"><div class="mon">DEC</div><div class="num">13</div></div><div><h3 class="event-title">Brew &amp; Connect - Elmbridge Market</h3><p class="event-meta"><svg viewBox="0 0 12 12"><circle cx="6" cy="6" r="5" fill="none" stroke="#333" stroke-width="1.2"/><path d="M6 3v3h2.5" fill="none" stroke="#333" stroke-width="1.2"/></svg>Tuesday ,10:00am - 11:30am</p><p class="event-meta"><svg viewBox="0 0 12 12"><path d="M6 11.5S2 7 2 4.5a4 4 0 0 1 8 0C10 7 6 11.5 6 11.5z" fill="#333"/><circle cx="6" cy="4.5" r="1.4" fill="#fff"/></svg>Elmbridge Market, Ferry Lane , Elmbridge , Elmbridge , EB4 7QT</p></div></article>
  <article class="event standard" style="top:1360px"><div class="date-box"><div class="mon">DEC</div><div class="num">13</div></div><div><h3 class="event-title">Brew &amp; Connect - Elmbridge Market</h3><p class="event-meta"><svg viewBox="0 0 12 12"><circle cx="6" cy="6" r="5" fill="none" stroke="#333" stroke-width="1.2"/><path d="M6 3v3h2.5" fill="none" stroke="#333" stroke-width="1.2"/></svg>Tuesday ,10:00am - 11:30am</p><p class="event-meta"><svg viewBox="0 0 12 12"><path d="M6 11.5S2 7 2 4.5a4 4 0 0 1 8 0C10 7 6 11.5 6 11.5z" fill="#333"/><circle cx="6" cy="4.5" r="1.4" fill="#fff"/></svg>Elmbridge Market, Ferry Lane , Elmbridge , Elmbridge , EB4 7QT</p></div></article>
  <article class="event standard" style="top:1459px"><div class="date-box"><div class="mon">DEC</div><div class="num">13</div></div><div><h3 class="event-title">Brew &amp; Connect - Elmbridge Market</h3><p class="event-meta"><svg viewBox="0 0 12 12"><circle cx="6" cy="6" r="5" fill="none" stroke="#333" stroke-width="1.2"/><path d="M6 3v3h2.5" fill="none" stroke="#333" stroke-width="1.2"/></svg>Tuesday ,10:00am - 11:30am</p><p class="event-meta"><svg viewBox="0 0 12 12"><path d="M6 11.5S2 7 2 4.5a4 4 0 0 1 8 0C10 7 6 11.5 6 11.5z" fill="#333"/><circle cx="6" cy="4.5" r="1.4" fill="#fff"/></svg>Elmbridge Market, Ferry Lane , Elmbridge , Elmbridge , EB4 7QT</p></div></article>
  <article class="event standard" style="top:1561px"><div class="date-box"><div class="mon">DEC</div><div class="num">13</div></div><div><h3 class="event-title">Brew &amp; Connect - Elmbridge Market</h3><p class="event-meta"><svg viewBox="0 0 12 12"><circle cx="6" cy="6" r="5" fill="none" stroke="#333" stroke-width="1.2"/><path d="M6 3v3h2.5" fill="none" stroke="#333" stroke-width="1.2"/></svg>Tuesday ,10:00am - 11:30am</p><p class="event-meta"><svg viewBox="0 0 12 12"><path d="M6 11.5S2 7 2 4.5a4 4 0 0 1 8 0C10 7 6 11.5 6 11.5z" fill="#333"/><circle cx="6" cy="4.5" r="1.4" fill="#fff"/></svg>Elmbridge Market, Ferry Lane , Elmbridge , Elmbridge , EB4 7QT</p></div></article>
  <article class="event standard" style="top:1666px"><div class="date-box"><div class="mon">DEC</div><div class="num">13</div></div><div><h3 class="event-title">Brew &amp; Connect - Elmbridge Market</h3><p class="event-meta"><svg viewBox="0 0 12 12"><circle cx="6" cy="6" r="5" fill="none" stroke="#333" stroke-width="1.2"/><path d="M6 3v3h2.5" fill="none" stroke="#333" stroke-width="1.2"/></svg>Tuesday ,10:00am - 11:30am</p><p class="event-meta"><svg viewBox="0 0 12 12"><path d="M6 11.5S2 7 2 4.5a4 4 0 0 1 8 0C10 7 6 11.5 6 11.5z" fill="#333"/><circle cx="6" cy="4.5" r="1.4" fill="#fff"/></svg>Elmbridge Market, Ferry Lane , Elmbridge , Elmbridge , EB4 7QT</p></div></article>

  <h2 class="section-title" style="left:734px;top:605px"><svg viewBox="0 0 20 20"><circle cx="10" cy="10" r="4" fill="none" stroke="#222" stroke-width="1.8"/><path d="M10 1v3M10 16v3M1 10h3M16 10h3M3.6 3.6l2.1 2.1M14.3 14.3l2.1 2.1M3.6 16.4l2.1-2.1M14.3 5.7l2.1-2.1" stroke="#222" stroke-width="1.8"/></svg>Ads</h2>
  <div class="ad-slot" role="img" aria-label="Advertisement space"></div>

  <h2 class="section-title" style="left:734px;top:906px"><svg viewBox="0 0 20 20"><path d="M3 8l3-4h8l3 4-7 9z" fill="none" stroke="#f28a14" stroke-width="2" stroke-linejoin="round"/><path d="M3 8h14" stroke="#f28a14" stroke-width="2"/></svg>Premium Profile</h2>
  <p class="promo-lead">Event Organisers - Upgrade to Premium Profile for only £4.99/month!</p>
  <p class="promo-body">Inclusion in Featured Events section and highlighting of your events, display of event photos and videos, direct booking and social networking links and more!</p>
  <a class="btn-outline">Find out more..</a>
</div>
</body>
</html>
```